Create Homepage Header & Search Box for Education Website

This project is relatively small and pays well.
Site: brightvalelearning.org
Project Title:
Redesign slider to be a static image/graphic and include a 3 drop down search box.
Project Summary:
We need a new homepage header for brightvalelearning.org. The logo, top navigation, and social buttons should remain unchanged. The new header needs to include a static graphic or image and a 3 drop down search box. It can also include some text that speaks to the what our site provides. For text suggestions - see below. Placement for the search box should be to the left under the logo. We will remove the slider functionality and need the design to be static.
Below the current slider images are bar graphs and a pie graph. These can remain as is - or you can make design changes. If you make design changes - please be sure the message doesn't change. Also you can submit one version of the design with this removed if you feel like it helps best accomplish our goal of conversion.
Project Objectives:
The primary objective of the deign is to maximize conversion of clicks to the search box. We need users to gravitate to the search box. Additionally the design should convey trust and academic feel.
Target Market:
High School Graduates and people in their 20s looking for college options.
Potential text:
Tagline Option: "Your #1 Resource for an Affordable Online College Education"
Tagline Option: "Find Affordable Online College Options"
Other Details: Brightvale Learning Hub will help you find a more affordable college experience. Look no further to find financial aid information, cost saving tips, and comprehensive college rankings focused on affordability and value.
Or you can also use some placeholder text and I can create the right messaging.
The Search Box:
The search box is pretty standard - you can see examples in the examples below - or in the files I attached. 3 drop downs and a "Search" button.
Examples of some previous designs attached to the project:
These designs are close - but not perfect. These will give you a good general idea for what we need.
Examples of designs at similar websites:
kwpn.org
studyharborhub.net
topmeadowcourses.com

```html
<!DOCTYPE html>
<html lang="en">
<head>
<meta charset="utf-8">
<title>Brightvale Learning Hub — Home</title>
<link href="https://fonts.googleapis.com/css2?family=Oswald:wght@400;500;700&family=Open+Sans:wght@400;600&family=Yanone+Kaffeesatz:wght@300;400&family=Bebas+Neue&display=swap" rel="stylesheet">
<style>
  :root{
    --orange:#f3782a;
    --orange-deep:#ee5f22;
    --orange-light:#f89a3a;
    --teal:#1c6462;
    --teal-edge:#3c8a86;
    --teal-soft:#7aaba7;
    --teal-dark:#124544;
    --night:#1b2327;
    --ink:#444;
    --muted:#777;
    --white:#fff;
    --sun:#f0a21e;
  }
  *{box-sizing:border-box;margin:0;padding:0}
  html,body{width:1200px;height:707px;overflow:hidden;background:var(--white);font-family:"Open Sans",sans-serif}
  .page{position:relative;width:1200px;height:707px;overflow:hidden}

  /* header */
  .brand{position:absolute;left:156px;top:0;width:92px;height:92px;border-radius:50%;background:var(--orange-deep);border:3px solid var(--white);box-shadow:0 2px 5px rgba(0,0,0,.3);z-index:3;display:flex;align-items:center;justify-content:center;text-align:center;color:var(--white);font-family:"Open Sans",sans-serif;font-weight:600;font-size:11px;line-height:13px;padding:0 10px}
  .nav{position:absolute;left:318px;top:26px;display:flex;font-size:13.5px;letter-spacing:.8px;color:var(--ink)}
  .nav a{color:inherit;text-decoration:none;position:absolute;white-space:nowrap}
  .nav a.active{color:var(--orange)}
  .nav a.active::after{content:"";position:absolute;left:0;right:0;top:21px;height:2px;background:var(--orange)}
  .social{position:absolute;left:895px;top:25px;display:flex;gap:13px}
  .social span{width:20px;height:20px;border-radius:3px;display:block}

  /* hero */
  .hero{position:absolute;left:0;top:65px;width:1200px;height:290px;background:radial-gradient(ellipse at 60% 55%,var(--orange-light),var(--orange) 55%,var(--orange-deep));box-shadow:inset 0 3px 4px rgba(0,0,0,.12)}
  .search-panel{position:absolute;left:143px;top:106px;width:400px;height:232px}
  .search-title{position:absolute;left:180px;top:116px;font-family:"Oswald",sans-serif;font-weight:500;font-size:38px;letter-spacing:7px;color:var(--white)}
  .select{position:absolute;left:179px;width:231px;height:35px;background:var(--teal-soft);color:var(--white);font-family:"Yanone Kaffeesatz",sans-serif;font-size:21px;display:flex;align-items:center;padding-left:38px;letter-spacing:.5px}
  .select .num{position:absolute;left:5px;top:5px;width:25px;height:25px;border-radius:50%;background:var(--orange-deep);border:2px solid var(--white);font-size:15px;display:flex;align-items:center;justify-content:center}
  .select .caret{position:absolute;right:9px;top:13px;width:0;height:0;border-left:7px solid transparent;border-right:7px solid transparent;border-top:10px solid var(--teal-dark)}
  .search-btn{position:absolute;left:424px;top:180px;width:88px;height:88px}
  .headline{position:absolute;left:560px;top:112px;width:590px;text-align:center;color:var(--white);text-shadow:1px 2px 3px rgba(0,0,0,.35)}
  .headline h1{font-family:"Bebas Neue",sans-serif;font-weight:400;font-size:74px;letter-spacing:7px;line-height:74px}
  .headline h2{font-family:"Bebas Neue",sans-serif;font-weight:400;font-size:32px;letter-spacing:1px;line-height:32px;margin-top:-4px}
  .headline p{font-family:"Bebas Neue",sans-serif;font-size:21px;letter-spacing:1.2px;line-height:25px;margin-top:18px}

  /* stats */
  .stats{position:absolute;left:65px;top:355px;width:1040px;height:112px;background:var(--night);box-shadow:0 2px 4px rgba(0,0,0,.35)}
  .bar{position:absolute;left:70px;width:150px;height:34px;border:1px solid #2c3a3e;background:#141b1e}
  .bar .fill{position:absolute;left:0;top:0;bottom:0;background:var(--teal)}
  .bar .val{position:absolute;left:20px;top:1px;font-family:"Oswald",sans-serif;font-size:21px;color:var(--white)}
  .stat-label{position:absolute;font-family:"Oswald",sans-serif;font-size:15px;color:var(--orange);letter-spacing:-.3px;line-height:19px;text-transform:uppercase}
  .pie{position:absolute;left:420px;top:13px;width:78px;height:78px}
  .stats-note{position:absolute;left:640px;top:18px;width:340px;text-align:center;color:var(--white);font-size:13px;line-height:19px}
  .stats-note h3{font-weight:400;font-size:14.5px;color:var(--orange);margin-bottom:5px}

  /* features */
  .feature{position:absolute;width:270px}
  .feature .icon{position:absolute;left:0;top:0;width:70px;height:70px;border-radius:50%;background:var(--orange-deep);display:flex;align-items:center;justify-content:center}
  .feature h4{position:absolute;left:82px;top:-4px;width:190px;font-weight:400;font-size:14.5px;line-height:19px;color:var(--ink)}
  .feature p{position:absolute;left:82px;width:180px;font-size:10.5px;line-height:18px;color:var(--muted)}
  .feature .more{position:absolute;width:66px;height:20px;border:1px solid #ddd;border-radius:2px;font-size:9.5px;color:var(--orange-deep);display:flex;align-items:center;justify-content:center;box-shadow:0 1px 2px rgba(0,0,0,.12)}
</style>
</head>
<body>
<div class="page">

  <div class="brand">Brightvale Learning Hub</div>

  <nav class="nav">
    <a class="active" style="left:0">Home</a>
    <a style="left:71px">Financial Aid</a>
    <a style="left:192px">Cost Savings</a>
    <a style="left:314px">Colleges</a>
    <a style="left:405px">Awards</a>
    <a style="left:486px">Blog</a>
  </nav>
  <div class="social">
    <span style="background:#3b5998"></span>
    <span style="background:#1da1f2"></span>
    <span style="background:#d8332a"></span>
  </div>

  <section class="hero" role="img" aria-label="Orange background with soft flowing light lines"></section>

  <svg class="search-panel" viewBox="0 0 400 232" aria-hidden="true">
    <polygon points="2,2 342,2 397,114 342,230 2,230" fill="var(--teal)" stroke="var(--teal-edge)" stroke-width="3"/>
  </svg>
  <div class="search-title">QUICK SEARCH</div>
  <div class="select" style="top:172px"><span class="num">1.</span>Choose a Degree level<span class="caret"></span></div>
  <div class="select" style="top:222px"><span class="num">2.</span>Choose a Category<span class="caret"></span></div>
  <div class="select" style="top:271px"><span class="num">3.</span>Choose a Subject<span class="caret"></span></div>

  <svg class="search-btn" viewBox="0 0 88 88" aria-label="Search now">
    <defs><path id="ring" d="M44,44 m-31,0 a31,31 0 1,1 62,0 a31,31 0 1,1 -62,0"/></defs>
    <circle cx="44" cy="44" r="42" fill="var(--orange-deep)" stroke="var(--white)" stroke-width="2"/>
    <text font-family="Oswald,sans-serif" font-size="11" fill="var(--white)" letter-spacing="1.5"><textPath href="#ring">SEARCH NOW · SEARCH NOW ·</textPath></text>
    <circle cx="44" cy="44" r="18" fill="var(--sun)" stroke="var(--white)" stroke-width="3"/>
  </svg>

  <div class="headline">
    <h1>Your #1 Resource</h1>
    <h2>For an Affordable Online College Education</h2>
    <p>Brightvale Learning Hub will help you find a more affordable college experience. Look no further to find financial aid information, cost saving tips, and comprehensive college rankings focused on affordability and value.</p>
  </div>

  <section class="stats">
    <div class="bar" style="top:16px"><div class="fill" style="width:85px"></div><span class="val">$12,500</span></div>
    <div class="bar" style="top:60px"><div class="fill" style="width:125px"></div><span class="val">$26,600</span></div>
    <div class="stat-label" style="left:240px;top:23px">Avg student debt in 1996</div>
    <div class="stat-label" style="left:240px;top:67px">Avg student debt in 2011</div>
    <svg class="pie" viewBox="0 0 78 78" aria-label="66 percent pie chart">
      <circle cx="39" cy="39" r="38" fill="var(--teal)"/>
      <path d="M39,39 L39,1 A38,38 0 0,0 6,58 Z" fill="#26343a"/>
      <text x="39" y="46" text-anchor="middle" font-family="Oswald,sans-serif" font-size="20" fill="var(--white)">66%</text>
    </svg>
    <div class="stat-label" style="left:510px;top:38px">Pct of students<br>with loans</div>
    <div class="stats-note">
      <h3>College Costs Rising &amp; Student Debt Ballooning</h3>
      Brightvale Learning Hub helps students find affordable college options and provides information about financial aid and college rankings.
    </div>
  </section>

  <div class="feature" style="left:153px;top:508px">
    <div class="icon"><svg width="40" height="40" viewBox="0 0 40 40"><text x="20" y="32" text-anchor="middle" font-family="Oswald,sans-serif" font-size="34" fill="#fff">$</text></svg></div>
    <h4>Financial Aid</h4>
    <p style="top:28px">The nuts of bolts of financial aid – what's available and how to apply.</p>
    <span class="more" style="left:200px;top:72px">Read more</span>
  </div>

  <div class="feature" style="left:445px;top:508px">
    <div class="icon"><svg width="44" height="40" viewBox="0 0 44 40" fill="#fff">
      <rect x="4" y="26" width="7" height="12"/><rect x="14" y="20" width="7" height="18"/><rect x="24" y="14" width="7" height="24"/><rect x="34" y="8" width="7" height="30"/>
      <polyline points="3,18 14,10 22,12 38,2" fill="none" stroke="#fff" stroke-width="2.5"/></svg></div>
    <h4>Rising College Costs: Who is Helping?</h4>
    <p style="top:47px">Who's helping and what does that mean for you?</p>
    <span class="more" style="left:200px;top:90px">Read more</span>
  </div>

  <div class="feature" style="left:737px;top:508px">
    <div class="icon"><svg width="40" height="36" viewBox="0 0 40 36">
      <ellipse cx="20" cy="18" rx="16" ry="13" fill="#fff"/>
      <text x="20" y="24" text-anchor="middle" font-family="Oswald,sans-serif" font-size="16" fill="var(--orange-deep)">$</text></svg></div>
    <h4>Affordability Tips</h4>
    <p style="top:28px">Check out our tips for how you can make college more affordable</p>
    <span class="more" style="left:200px;top:72px">Read more</span>
  </div>

  <div class="feature" style="left:153px;top:694px"><div class="icon"></div><h4>Affordable Campus Colleges</h4></div>
  <div class="feature" style="left:445px;top:694px"><div class="icon"></div><h4>Awards</h4></div>
  <div class="feature" style="left:737px;top:694px"><div class="icon"></div><h4>Blog</h4></div>

</div>
</body>
</html>
```